business card Quintavo

Wee need a business card design for a new compagny based on Paris
We developped innovative a platform for selling services to refresh, beautify and develop its housing.
We would like a red logo on a black background
Te final design should communicate quality service, know-how, high-end

Target Market(s)

individuals

Industry/Entity Type

Business

```html
<!DOCTYPE html>
<html lang="en">
<head>
<meta charset="utf-8">
<title>Quintavo business card</title>
<link href="https://fonts.googleapis.com/css2?family=Open+Sans:wght@300;400;700&display=swap" rel="stylesheet">
<style>
  :root {
    --page: #e2e2e2;
    --card: #0e0e0f;
    --card-sheen: #1d1d1f;
    --coral: #e8716b;
    --grey: #8c8b8b;
    --brand-grey: #9a9a9a;
    --text: #f2f2f2;
    --rule: #5a5a5a;
  }
  * { box-sizing: border-box; margin: 0; padding: 0; }
  html, body {
    width: 1200px; height: 852px; overflow: hidden;
    background: var(--page);
    font-family: "Open Sans", Arial, sans-serif;
  }
  .canvas { position: relative; width: 1200px; height: 852px; }

  .card {
    position: absolute;
    width: 560px; height: 320px;
    border-radius: 24px;
    overflow: hidden;
    background: linear-gradient(115deg, var(--card) 0%, var(--card) 40%, var(--card-sheen) 55%, var(--card) 75%);
    box-shadow: 0 10px 24px rgba(0,0,0,0.28);
  }
  .card--front { left: 70px; top: 80px; }
  .card--back  { left: 570px; top: 452px; }

  .brand {
    position: absolute;
    display: flex; align-items: center;
    color: var(--brand-grey);
    font-weight: 300;
    letter-spacing: 0.5px;
  }
  .brand__square { background: var(--coral); flex: none; }
  .card--front .brand { left: 150px; top: 128px; font-size: 54px; }
  .card--front .brand__square { width: 60px; height: 60px; margin-right: 12px; }
  .card--back .brand { left: 40px; top: 140px; font-size: 38px; }
  .card--back .brand__square { width: 40px; height: 40px; margin-right: 10px; }

  .divider {
    position: absolute; left: 262px; top: 24px;
    width: 1px; height: 230px;
    background: linear-gradient(var(--rule), rgba(90,90,90,0.2));
  }

  .contact { position: absolute; left: 284px; top: 30px; color: var(--text); }
  .contact__name { color: var(--coral); font-weight: 700; font-size: 17px; line-height: 1.2; }
  .contact__role { font-size: 11px; margin-top: 2px; }
  .contact__list { list-style: none; margin-top: 18px; font-size: 13px; line-height: 19px; }
  .contact__list li { display: flex; align-items: center; }
  .contact__list svg { width: 12px; height: 12px; margin-right: 10px; flex: none; fill: var(--coral); }
  .contact__list .no-icon { padding-left: 22px; }
  .contact__address { margin-top: 6px; font-size: 13px; line-height: 19px; }

  .band-coral {
    position: absolute; left: 0; bottom: 0;
    width: 320px; height: 14px;
    background: var(--coral);
  }
  .band-web {
    position: absolute; right: 0; bottom: 0;
    width: 250px; height: 58px;
    background: var(--grey);
    color: var(--text);
    font-size: 14px;
    display: flex; align-items: center; padding-left: 24px;
  }
</style>
</head>
<body>
<div class="canvas">

  <section class="card card--front">
    <div class="brand"><span class="brand__square"></span>Quintavo</div>
  </section>

  <section class="card card--back">
    <div class="brand"><span class="brand__square"></span>Quintavo</div>
    <div class="divider"></div>

    <div class="contact">
      <p class="contact__name">Your Long Name</p>
      <p class="contact__role">Managing Director</p>
      <ul class="contact__list">
        <li><svg viewBox="0 0 12 12"><path d="M1 3c0-1 1-2 2-2h1l1 3-1.5 1c.6 1.4 1.6 2.4 3 3l1-1.5 3 1v1c0 1-1 2-2 2C4.5 11.5.5 7.5 1 3z"/></svg>00.00.00.0000</li>
        <li class="no-icon">00.00.00.0000</li>
        <li><svg viewBox="0 0 12 12"><rect x="3" y="0.5" width="6" height="11" rx="1.2"/><rect x="4" y="2" width="4" height="7" fill="#0e0e0f"/></svg>yourname@yourwebsite.com</li>
        <li><svg viewBox="0 0 12 12"><rect x="0.5" y="2" width="11" height="8" rx="1"/><path d="M1 2.5l5 4 5-4" stroke="#0e0e0f" stroke-width="1.2" fill="none"/></svg>Your Commercial or office address</li>
        <li class="no-icon">in just two line with pincode</li>
      </ul>
    </div>

    <div class="band-coral"></div>
    <div class="band-web">www.yourwebsite.com</div>
  </section>

</div>
</body>
</html>
```